Realty Group Needs Classy, Contemporary Letterhead Design

We need a letterhead design for a new realty company located in NY, USA. We buy investment properties to rehabilitate and or keep in our rental portfolio.

```html
<!DOCTYPE html>
<html lang="en">
<head>
<meta charset="utf-8">
<title>Halverton Letterhead</title>
<link rel="stylesheet" href="https://fonts.googleapis.com/css2?family=Montserrat:wght@800&family=Open+Sans:wght@400;700&family=Roboto+Condensed:wght@400&display=swap">
<style>
  :root {
    --brand-purple: #4f2d84;
    --backdrop: #bdbebf;
    --paper: #ffffff;
    --ink: #555558;
    --ink-dark: #444447;
  }
  * { margin: 0; padding: 0; box-sizing: border-box; }
  html, body {
    width: 1200px; height: 1164px; overflow: hidden;
    background: var(--backdrop);
  }
  .letterhead {
    position: absolute; left: 235px; top: 85px;
    width: 730px; height: 1032px;
    background: var(--paper);
    font-family: "Open Sans", Arial, sans-serif;
    color: var(--ink);
  }
  .corner-accent { position: absolute; left: 0; top: 0; }
  .edge-bar {
    position: absolute; right: 0; top: 0;
    width: 15px; height: 823px;
    background: var(--brand-purple);
  }
  .base-bar {
    position: absolute; left: 0; bottom: 0;
    width: 469px; height: 12px;
    background: var(--brand-purple);
  }
  .brand-name {
    position: absolute; left: 375px; top: 92px;
    font-family: "Montserrat", Arial, sans-serif;
    font-weight: 800; font-size: 31px; letter-spacing: -0.5px;
    color: var(--brand-purple);
  }
  .letter {
    position: absolute; left: 134px; top: 194px; width: 443px;
    font-size: 12.2px; line-height: 20.8px;
  }
  .recipient { margin-bottom: 20px; }
  .body-text { text-align: justify; line-height: 19.6px; }
  .closing { margin-bottom: 20px; }
  .signature-name { font-weight: 700; color: var(--ink-dark); }
  .contact-strip {
    position: absolute; left: 134px; top: 843px;
    display: flex; gap: 0;
  }
  .contact-item {
    display: flex; align-items: center; gap: 6px;
    width: 125px;
    font-family: "Roboto Condensed", Arial, sans-serif;
    font-size: 7.4px; line-height: 9.5px; color: var(--ink);
  }
  .contact-item svg { flex: none; }
</style>
</head>
<body>
  <main class="letterhead">
    <svg class="corner-accent" width="140" height="280" viewBox="0 0 140 280" aria-hidden="true">
      <polygon points="0,0 132,0 56,64 56,235 0,275" fill="var(--brand-purple)"/>
      <g stroke="var(--paper)" stroke-width="4">
        <line x1="0" y1="101" x2="58" y2="60"/>
        <line x1="0" y1="161" x2="58" y2="120"/>
        <line x1="0" y1="221" x2="58" y2="180"/>
      </g>
    </svg>
    <div class="edge-bar"></div>
    <div class="base-bar"></div>

    <div class="brand-name">HALVERTON</div>

    <section class="letter">
      <address class="recipient" style="font-style: normal;">
        Mara Quill<br>Title<br>Company Name<br>4321 First Street<br>Anytown, State ZIP<br>Date 1/30/12
      </address>
      <p>Dear Mara,</p>
      <div class="body-text">
        <p>Lorem ipsum dolor sit amet, consectetur adipiscing elit, set eiusmod tempor incidunt et labore et dolore magna aliquam. Ut enim ad minim veniam, quis nostrud exerc. Irure dolor in reprehend incididunt ut labore et dolore magna aliqua. Ut enim ad minim is nostrud exercitation ullam mmodo consequet. Duis aute in voluptate velit esse cillum dolore eu fugiat nulla pariatur.</p>
        <p>At vver eos et accusam dignissum qui blandit est praesent. Mara quill beynoc-guon doas nog apoply su trenz ucu hugh rasoluguon monugor or trenz ucugwo jag scannar. Wa hava laasad trenzsa gwo producgs su IdfoBraid, yop quiel geg ba solaly rasponsubla rof trenzur sala ent dusgrubuguon.</p>
        <p>Plloaso mako nuto uf cakso dodtos anr koop a cupy uf cak vux noaw yerw phuno. Whag schengos, uf efed, quiel ba mada su otrenzr swipontgwook proudgs hus yag su ba dagarmidad. Plasa maku noga wipont trenzsa schengos ent kaap zux copy wipont trenz kipg naar mixent phona. Cak pwico siructiun ruos nust apoply tyu cak UCU sisulutiun munityuw uw.</p>
      </div>
      <p class="closing">Sincerely yours,</p>
      <p class="signature-name">OWNER NAME</p>
      <p class="signature-title">MANAGER</p>
    </section>

    <footer class="contact-strip">
      <div class="contact-item">
        <svg width="24" height="26" viewBox="0 0 24 26" aria-hidden="true">
          <polygon points="12,0 24,6.5 24,19.5 12,26 0,19.5 0,6.5" fill="var(--brand-purple)"/>
          <path d="M8 7.5c.6-.5 1.3-.4 1.6.2l1 1.8c.2.5 0 1-.4 1.3l-.7.5c.6 1.4 1.6 2.5 3 3.1l.5-.7c.3-.4.9-.6 1.3-.4l1.8 1c.6.3.7 1 .2 1.6-1 1.2-2.3 1.4-3.8.6-2.3-1.2-4-3-5-5.3-.6-1.5-.4-2.9.5-3.7z" fill="var(--paper)"/>
        </svg>
        <span>+000 000 000 00<br>+000 000 000 00</span>
      </div>
      <div class="contact-item">
        <svg width="24" height="26" viewBox="0 0 24 26" aria-hidden="true">
          <polygon points="12,0 24,6.5 24,19.5 12,26 0,19.5 0,6.5" fill="var(--brand-purple)"/>
          <rect x="6.5" y="9" width="11" height="8" fill="var(--paper)"/>
          <path d="M6.5 9l5.5 4.5L17.5 9" fill="none" stroke="var(--brand-purple)" stroke-width="1"/>
        </svg>
        <span>hello@halverton.co<br>info@halverton.co</span>
      </div>
      <div class="contact-item">
        <svg width="24" height="26" viewBox="0 0 24 26" aria-hidden="true">
          <polygon points="12,0 24,6.5 24,19.5 12,26 0,19.5 0,6.5" fill="var(--brand-purple)"/>
          <g fill="none" stroke="var(--paper)" stroke-width="1.1">
            <circle cx="12" cy="13" r="5.5"/>
            <ellipse cx="12" cy="13" rx="2.4" ry="5.5"/>
            <line x1="6.5" y1="13" x2="17.5" y2="13"/>
          </g>
        </svg>
        <span>www.halverton.co<br>www.halverton.net</span>
      </div>
      <div class="contact-item">
        <svg width="24" height="26" viewBox="0 0 24 26" aria-hidden="true">
          <polygon points="12,0 24,6.5 24,19.5 12,26 0,19.5 0,6.5" fill="var(--brand-purple)"/>
          <path d="M12 19.5s-4.5-4.6-4.5-7.8a4.5 4.5 0 0 1 9 0c0 3.2-4.5 7.8-4.5 7.8z" fill="var(--paper)"/>
          <circle cx="12" cy="11.7" r="1.6" fill="var(--brand-purple)"/>
        </svg>
        <span>Street, Region<br>Country 11000</span>
      </div>
    </footer>
  </main>
</body>
</html>
```